Keep the Sunny Side Up!!! Business Card Design

We need a business card for new company based in Denver CO called Sunny Side Goods, Inc. ( would prefer to use Keep the Sunny Side Up!!! on the card instead of the company name) The logo and theme for the company is Keep the Sunny Side Up!!! (See logo image).We want to create a lifestyle company (like Joy Runs Deep) with a positive view on life. My first product that we will be selling is a Keep the Sunny Side Up!!! Bag (see tag image). The first uses for the bag would be for the beach, concerts and picnics. Going forward I would like to make other merchandise that would continue on the theme of motivating and helping people Make it a Great Day!!!Designs with brighter uplifting colors would be preferred. Want to convey the message of Keep the Sunny Side Up!!! in the final design.
Updates

Project Deadline Extended
Reason: I would like to guarantee that everyone has had time to submit their final designs. Keep the Sunny Side Up!!! Rob

Target Market(s)

Women who love stuffing stuff in bags to go to places and still want to be able to use their arms for other things like holding their children or talking on the phone.

Industry/Entity Type

Business

Contact Information for Business Card

Rob GodzichFounderOffice Phone: (720) 663-8739Cell Phone: (612) 501-2545Email: rvanterpool@sunnysidegoods-example.com

Font styles to use
Decorative

Requirements
Must have
• Must convey a positive message and get people to be inspired to Keep the Sunny Side Up!!!

```html
<!DOCTYPE html>
<html lang="en">
<head>
<meta charset="utf-8">
<title>Keep the Sunny Side Up!!! – Business Card</title>
<link rel="stylesheet" href="https://fonts.googleapis.com/css2?family=Exo+2:wght@400;500;600&display=swap">
<style>
  :root {
    --sun-orange: #e8681f;
    --card-white: #ffffff;
    --card-mist: #e6e7e9;
    --rim-grey: #b9bbbe;
    --ink: #2b2b2b;
    --ink-soft: #3c3c3c;
    --page: #dfe2e6;
  }
  * { margin: 0; padding: 0; box-sizing: border-box; }
  html, body {
    width: 1200px;
    height: 864px;
    overflow: hidden;
    background: var(--page);
    font-family: "Exo 2", sans-serif;
  }
  .business-card {
    position: absolute;
    left: 100px;
    top: 142px;
    width: 1000px;
    height: 580px;
    background: radial-gradient(ellipse at 45% 35%, var(--card-white) 0%, var(--card-white) 45%, var(--card-mist) 100%);
    box-shadow: 0 10px 30px rgba(0, 0, 0, 0.18);
    overflow: hidden;
  }
  .card-art {
    position: absolute;
    inset: 0;
    width: 100%;
    height: 100%;
  }
  .brand-mark {
    position: absolute;
    top: 34px;
    right: 48px;
    display: flex;
    align-items: center;
    gap: 12px;
    color: var(--sun-orange);
    font-weight: 600;
    font-size: 24px;
    letter-spacing: 0.3px;
  }
  .brand-dot {
    width: 26px;
    height: 26px;
    border-radius: 50%;
    background: var(--sun-orange);
  }
  .address {
    position: absolute;
    top: 88px;
    right: 48px;
    text-align: right;
    color: var(--ink);
    font-size: 19px;
    line-height: 1.3;
    letter-spacing: 0.6px;
  }
  .contact-list {
    position: absolute;
    top: 150px;
    right: 40px;
    list-style: none;
    color: var(--ink);
    font-size: 15px;
    letter-spacing: 0.6px;
  }
  .contact-list li {
    display: flex;
    align-items: center;
    justify-content: flex-end;
    gap: 10px;
    height: 28px;
  }
  .contact-icon {
    width: 16px;
    height: 16px;
    flex: none;
    fill: var(--sun-orange);
  }
  .person {
    position: absolute;
    left: 48px;
    bottom: 72px;
  }
  .person-name {
    color: var(--card-white);
    font-size: 30px;
    font-weight: 500;
    letter-spacing: 1px;
    text-transform: uppercase;
  }
  .person-role {
    color: var(--ink-soft);
    font-size: 20px;
    letter-spacing: 0.8px;
    margin-top: 2px;
  }
</style>
</head>
<body>
  <main class="business-card">
    <svg class="card-art" viewBox="0 0 1000 580" preserveAspectRatio="none" aria-hidden="true">
      <path class="orange-field" fill="#e8681f"
        d="M0,120 L270,40 C150,110 170,250 330,300 C500,350 800,345 1000,330 L1000,580 L0,580 Z"/>
      <path class="rim-swoosh" fill="#b9bbbe"
        d="M270,40 C150,110 170,250 330,300 C500,350 800,345 1000,330 L1000,316 C800,328 520,328 340,284 C200,230 190,110 270,40 Z"/>
    </svg>

    <div class="brand-mark">
      <span class="brand-dot"></span>
      <span class="brand-name">Keep the Sunny Side Up!!!</span>
    </div>

    <p class="address">1420 Larimer St, Suite 18<br>Denver, CO 80202</p>

    <ul class="contact-list">
      <li>(720) 555-0142
        <svg class="contact-icon" viewBox="0 0 16 16"><path d="M3 1l3 0 1 4-2 1c1 2 3 4 5 5l1-2 4 1 0 3c0 1-1 2-2 2C7 15 1 9 1 3c0-1 1-2 2-2z"/></svg>
      </li>
      <li>(612) 555-0187
        <svg class="contact-icon" viewBox="0 0 16 16"><path d="M4 0h8a1 1 0 0 1 1 1v14a1 1 0 0 1-1 1H4a1 1 0 0 1-1-1V1a1 1 0 0 1 1-1zm1 2v10h6V2zm3 11a1 1 0 1 0 0 2 1 1 0 0 0 0-2z"/></svg>
      </li>
      <li>(720) 555-0193
        <svg class="contact-icon" viewBox="0 0 16 16"><path d="M4 1h7v4H4zM1 6h14v7h-3v2H4v-2H1zm4 5v3h6v-3z"/></svg>
      </li>
      <li>rvanterpool@sunnysidegoods-example.com
        <svg class="contact-icon" viewBox="0 0 16 16"><path d="M1 3h14v10H1zm1 1v1l6 4 6-4V4z"/></svg>
      </li>
      <li>www.sunnysidegoods-example.com
        <svg class="contact-icon" viewBox="0 0 16 16"><circle cx="8" cy="8" r="7"/><path d="M1 8h14M8 1c3 3 3 11 0 14M8 1c-3 3-3 11 0 14" stroke="#fff" stroke-width="1" fill="none"/></svg>
      </li>
    </ul>

    <div class="person">
      <p class="person-name">Rob Vanterpool</p>
      <p class="person-role">Managing Director</p>
    </div>
  </main>
</body>
</html>
```